Wedding Ceremony Equipment Hire Business Card

I need a business card design for a new business I created called Vow Outfitters. We hire out Wedding Ceremony equipment and decorations mainly for beach and garden wedding ceremonies that include delivery, set up and dismantle. We do offer DIY Chair Hire as well.
I'd like to have a similar design and colours to our website:
www.vowoutfitters-example.com.au
If possible would like the front to incorporate our information and logo and the back to have two faded example pictures of our wedding ceremonies.
I have attached two photos and our logo. Please let me know if you need a better pic of our logo though.

Target Market(s)

Newly engaged couples, aged 25 and upwards

Industry/Entity Type

Wedding

Contact Information for Business Card

Vow Outfitters
Merel Thorpe
0491 870 264
vowoutfitters@mailbox-example.com
www.social-example.com/VowOutfitters

```html
<!DOCTYPE html>
<html lang="en">
<head>
<meta charset="utf-8">
<title>Vow Outfitters – Business Card</title>
<link rel="stylesheet" href="https://fonts.googleapis.com/css2?family=Cormorant+Garamond:ital,wght@0,600;1,500&family=Pinyon+Script&display=swap">
<style>
  :root {
    --stage: #2b2b2b;
    --mint: #a9d3c6;
    --mint-soft: #bfe0d5;
    --card-dark: #232323;
    --ink-dark: #1f1f1f;
    --ink-light: #f4f4f4;
    --ink-muted: #d9d9d9;
  }
  * { margin: 0; padding: 0; box-sizing: border-box; }
  html, body { width: 1200px; height: 900px; overflow: hidden; }
  body {
    background: var(--stage);
    display: flex;
    align-items: center;
    justify-content: center;
    gap: 40px;
  }
  .card {
    position: relative;
    width: 540px;
    height: 318px;
    overflow: hidden;
    box-shadow: 0 6px 18px rgba(0,0,0,0.45);
  }
  .card-front { background: var(--card-dark); }
  .card-back { background: var(--card-dark); display: flex; flex-direction: column; }
  .band {
    height: 86px;
    background: linear-gradient(100deg, var(--mint) 0%, var(--mint-soft) 55%, var(--mint) 100%);
    display: flex;
    align-items: center;
  }
  .card-front .band { padding-left: 26px; }
  .card-back .band { justify-content: center; }
  .brand-name {
    font-family: "Cormorant Garamond", Georgia, serif;
    font-weight: 600;
    font-style: normal;
    font-size: 30px;
    color: var(--ink-dark);
    letter-spacing: 0.5px;
  }
  .holder-name {
    position: absolute;
    left: 30px;
    top: 128px;
    font-family: "Pinyon Script", cursive;
    font-size: 34px;
    color: var(--ink-light);
  }
  .contact-list {
    position: absolute;
    left: 30px;
    top: 206px;
    list-style: none;
  }
  .contact-item {
    display: flex;
    align-items: center;
    gap: 10px;
    height: 22px;
    font-family: "Cormorant Garamond", Georgia, serif;
    font-style: italic;
    font-weight: 500;
    font-size: 14px;
    color: var(--ink-muted);
  }
  .contact-icon { width: 11px; height: 11px; flex: none; }
  .photo-row { flex: 1; display: flex; gap: 3px; }
  .photo { flex: 1; }
  .photo-beach {
    background: linear-gradient(180deg, #4d7fc4 0%, #8fb3da 38%, #e9e6e0 48%, #c9a57a 62%, #b48e63 100%);
  }
  .photo-garden {
    background: linear-gradient(180deg, #5a8fd0 0%, #9fc0df 32%, #6f8f4a 50%, #3f6a2a 78%, #2f5521 100%);
  }
</style>
</head>
<body>
  <section class="card card-front" aria-label="Business card front">
    <header class="band">
      <span class="brand-name">Vow Outfitters</span>
    </header>
    <p class="holder-name">Merel Thorpe</p>
    <ul class="contact-list">
      <li class="contact-item">
        <svg class="contact-icon" viewBox="0 0 12 12"><rect x="3" y="0.5" width="6" height="11" rx="1" fill="none" stroke="#d9d9d9" stroke-width="1.2"/><line x1="5" y1="9.5" x2="7" y2="9.5" stroke="#d9d9d9"/></svg>
        0491 870 264
      </li>
      <li class="contact-item">
        <svg class="contact-icon" viewBox="0 0 12 12"><rect x="0.5" y="2" width="11" height="8" fill="none" stroke="#d9d9d9" stroke-width="1.2"/><polyline points="0.5,2 6,6.5 11.5,2" fill="none" stroke="#d9d9d9" stroke-width="1.2"/></svg>
        vowoutfitters@mailbox-example.com
      </li>
      <li class="contact-item">
        <svg class="contact-icon" viewBox="0 0 12 12"><circle cx="6" cy="6" r="5.2" fill="none" stroke="#d9d9d9" stroke-width="1.2"/><ellipse cx="6" cy="6" rx="2.2" ry="5.2" fill="none" stroke="#d9d9d9"/><line x1="0.8" y1="6" x2="11.2" y2="6" stroke="#d9d9d9"/></svg>
        www.vowoutfitters-example.com.au
      </li>
      <li class="contact-item">
        <svg class="contact-icon" viewBox="0 0 12 12"><rect x="0.5" y="0.5" width="11" height="11" fill="#d9d9d9"/></svg>
        www.social-example.com/VowOutfitters
      </li>
    </ul>
  </section>

  <section class="card card-back" aria-label="Business card back">
    <header class="band">
      <span class="brand-name">Vow Outfitters</span>
    </header>
    <div class="photo-row">
      <div class="photo photo-beach" role="img" aria-label="Photo of a beach wedding ceremony with rows of white chairs on the sand beside the sea"></div>
      <div class="photo photo-garden" role="img" aria-label="Photo of a garden wedding ceremony with white chairs and an aisle runner on the lawn overlooking a harbour"></div>
    </div>
  </section>
</body>
</html>
```